Business Card Design Project Calbrook Foundation

Looking for business card options to match our concurrent logo project on pixel forum. We are a international humanitarian aid firm. We work in the non profit sector but operate more closely to a traditional for-profit investment firm. As such we would like equal tones in our branding materials, which includes are business cards.

Stand by for logo...
Updates

logo uploaded.

Target Market(s)

Adults in western speaking countries ages 18-40 that work primarily in the NGO and Business Administrative Career Field.

Industry/Entity Type

Non Profit

Font styles to use
Sans Serif

Requirements
Nice to have
• We would like all contact information on one side.

Company Name/Logo, Individual Name and Position on the other...

```html
<!DOCTYPE html>
<html lang="en">
<head>
<meta charset="UTF-8">
<title>Calbrook Foundation – Business Cards</title>
<link rel="stylesheet" href="https://fonts.googleapis.com/css2?family=Open+Sans:wght@300;400;600&display=swap">
<style>
  :root {
    --page-bg: #e9e7e3;
    --card-blue: #4257a8;
    --card-blue-light: #5068bb;
    --card-blue-dark: #34468c;
    --band-dark: #2a2a31;
    --text-white: #ffffff;
    --text-soft: #e4e7f2;
    --divider: rgba(255,255,255,0.45);
    --mark-grey: #c9cbd3;
  }
  * { box-sizing: border-box; margin: 0; padding: 0; }
  html, body { width: 1200px; height: 1200px; overflow: hidden; }
  body {
    background: var(--page-bg);
    font-family: "Open Sans", Arial, sans-serif;
    position: relative;
  }
  .card {
    position: absolute;
    left: 150px;
    width: 900px;
    height: 514px;
    overflow: hidden;
    background: radial-gradient(ellipse at 65% 30%, var(--card-blue-light) 0%, var(--card-blue) 45%, var(--card-blue-dark) 100%);
    box-shadow: 0 6px 18px rgba(0,0,0,0.25);
  }
  .card--front { top: 60px; }
  .card--back { top: 620px; }

  .brand {
    position: absolute;
    display: flex;
    align-items: center;
    color: var(--text-white);
    font-weight: 300;
  }
  .brand__square {
    background: var(--mark-grey);
    flex: none;
  }
  .brand__name { line-height: 1; }
  .brand__word { display: block; letter-spacing: 0.1em; }
  .brand__word--small { letter-spacing: 0.32em; margin-top: 10px; }

  .card--front .brand { left: 90px; top: 110px; gap: 34px; }
  .card--front .brand__square { width: 110px; height: 110px; }
  .card--front .brand__word { font-size: 86px; }
  .card--front .brand__word--small { font-size: 42px; }

  .card--front .card__strip {
    position: absolute; left: 0; right: 0; bottom: 0; height: 16px;
    background: var(--band-dark);
  }
  .person {
    position: absolute; left: 150px; top: 330px;
    color: var(--text-white); font-size: 30px; line-height: 1.4;
    text-align: center;
  }
  .card__divider {
    position: absolute; left: 345px; top: 300px;
    width: 2px; height: 150px; background: var(--divider);
  }
  .contact {
    position: absolute; left: 395px; top: 300px;
    list-style: none; color: var(--text-white); font-size: 27px; line-height: 1.45;
  }
  .contact__item { display: flex; align-items: center; gap: 12px; }
  .contact__icon { width: 24px; height: 24px; fill: var(--text-white); flex: none; }

  .card--back .brand { left: 150px; top: 70px; gap: 40px; }
  .card--back .brand__square { width: 130px; height: 130px; }
  .card--back .brand__word { font-size: 96px; }
  .card--back .brand__word--small { font-size: 46px; }

  .card__band {
    position: absolute; left: 0; right: 0; bottom: 0; height: 160px;
    background: var(--band-dark);
  }
  .website {
    position: absolute; left: 34px; top: 24px;
    color: var(--text-white); font-size: 30px;
  }
  .follow {
    position: absolute; right: 34px; bottom: 30px;
    display: flex; align-items: center; gap: 16px;
    color: var(--text-soft); font-size: 28px;
  }
  .follow__network {
    background: var(--card-blue);
    color: var(--text-white);
    font-size: 20px;
    padding: 6px 12px;
  }
</style>
</head>
<body>

<section class="card card--front" aria-label="Business card front">
  <div class="brand">
    <span class="brand__square"></span>
    <span class="brand__name">
      <span class="brand__word">Calbrook</span>
      <span class="brand__word brand__word--small">FOUNDATION</span>
    </span>
  </div>

  <p class="person">Name<br>Title</p>
  <span class="card__divider"></span>

  <ul class="contact">
    <li class="contact__item">
      <svg class="contact__icon" viewBox="0 0 24 24" aria-hidden="true"><path d="M6.6 10.8c1.4 2.8 3.8 5.1 6.6 6.6l2.2-2.2c.3-.3.7-.4 1-.2 1.1.4 2.3.6 3.6.6.6 0 1 .4 1 1V20c0 .6-.4 1-1 1C10.6 21 3 13.4 3 4c0-.6.4-1 1-1h3.5c.6 0 1 .4 1 1 0 1.3.2 2.5.6 3.6.1.3 0 .7-.2 1l-2.3 2.2z"/></svg>
      <span>mobile</span>
    </li>
    <li class="contact__item">
      <svg class="contact__icon" viewBox="0 0 24 24" aria-hidden="true"><path d="M2 5h20v14H2z M2 5l10 8 10-8" fill="none" stroke="#fff" stroke-width="2"/><path d="M2 5h20l-10 8z"/></svg>
      <span>email</span>
    </li>
    <li class="contact__item">
      <svg class="contact__icon" viewBox="0 0 24 24" aria-hidden="true"><g fill="none" stroke="#fff" stroke-width="1.6"><circle cx="12" cy="12" r="9"/><ellipse cx="12" cy="12" rx="4" ry="9"/><path d="M3 12h18M5 7h14M5 17h14"/></g></svg>
      <span>web address</span>
    </li>
  </ul>

  <span class="card__strip"></span>
</section>

<section class="card card--back" aria-label="Business card back">
  <div class="brand">
    <span class="brand__square"></span>
    <span class="brand__name">
      <span class="brand__word">Calbrook</span>
      <span class="brand__word brand__word--small">FOUNDATION</span>
    </span>
  </div>

  <div class="card__band">
    <p class="website">www.website</p>
    <div class="follow">
      <span>Follow us on</span>
      <span class="follow__network">Friendbook</span>
      <span class="follow__network">Chirper</span>
    </div>
  </div>
</section>

</body>
</html>
```